Roll-up BETON IMPRIME

(Title): BETON IMPRIME
(Catch phrase): Des sols uniques
(Bullet points):
Aménagements urbains
Terrasses
Parcs à thèmes
Plages Piscines
Allées
Grand nombre de couleurs et textures...des milliers de possibilités
Our logo (SOLIDE TRAJET ...) well visible.
RVQL Logo (small at the bottom of the roll-up somewhere with a small text right on top of logo saying: "Classement performanciel". Just to hve it, but not part of the main design.
Picture BE Rond point needs to be zoomed a little to better show texture
Picture DSCN: cut out the ugly fence + left jobsite vision
Picture formation: cross out and state: "Fini les pavés qui déchaussent !"
(just fyi so you understand the comment while doing the design; because our solution makes a monolythic slab that cannot lift).
Roll-up is going to be used in show-rooms to explain what stamped concrete is about. We need something classy and modern.
Dimension of roll-up image: 85.2x220.2:
Good luck
Target Market(s)
architects, homeowners, contractors
Industry/Entity Type
Concrete
Look and feel

```html
<!DOCTYPE html>
<html lang="fr">
<head>
<meta charset="utf-8">
<title>Roll-up Béton Imprimé – Solide Trajet</title>
<link rel="stylesheet" href="https://fonts.googleapis.com/css2?family=Oswald:wght@500;600&family=Saira+Condensed:wght@400;500;600;700&family=Saira:wght@700;800&display=swap">
<style>
  :root {
    --bg-top: #f2f2f2;
    --bg-bottom: #dcdcdc;
    --ink-grey: #555659;
    --ink-dark: #3e3f42;
    --brand-blue: #1a5aa8;
    --deep-blue: #0e4b9a;
    --tag-dark: #4a4b4e;
    --tag-green: #13935a;
    --tag-blue: #1558a7;
    --tag-orange: #ef8410;
    --tag-grey: #a3a4a6;
    --rule: #b9b9bb;
    --cross-red: #e0262a;
  }
  * { margin: 0; padding: 0; box-sizing: border-box; }
  html, body { width: 1200px; height: 3097px; overflow: hidden; }
  body {
    position: relative;
    background: linear-gradient(180deg, var(--bg-top) 0%, #e4e4e4 50%, var(--bg-bottom) 100%);
    font-family: "Saira Condensed", "Arial Narrow", sans-serif;
    color: var(--ink-dark);
  }
  .abs { position: absolute; white-space: nowrap; }

  /* Brand banner */
  .brand-banner { left: 258px; top: 0; width: 684px; height: 310px; }
  .brand-name {
    left: 258px; top: 100px; width: 684px; text-align: center;
    font-family: "Saira", sans-serif; font-weight: 800; font-size: 64px;
    color: var(--brand-blue); letter-spacing: 1px;
  }
  .brand-tagline {
    left: 258px; top: 188px; width: 684px; text-align: center;
    font-weight: 600; font-size: 40px; color: #7b7c7f;
  }

  /* Title */
  .title-beton {
    left: 250px; top: 315px;
    font-family: "Oswald", sans-serif; font-weight: 600; font-size: 250px;
    line-height: 1; color: var(--ink-grey); letter-spacing: -4px;
  }
  .title-imprime {
    left: 250px; top: 580px; width: 700px; text-align: center;
    font-family: "Saira", sans-serif; font-weight: 800; font-size: 128px;
    line-height: 1; color: var(--brand-blue); letter-spacing: 8px;
  }
  .catchphrase {
    left: 0; top: 705px; width: 1200px; text-align: center;
    font-weight: 500; font-size: 50px; letter-spacing: 26px; text-indent: 26px;
    color: var(--ink-dark); text-transform: uppercase;
  }

  /* Intro band */
  .intro-band {
    left: 0; top: 805px; width: 1200px; height: 252px;
    background: linear-gradient(180deg, #d6d6d8 0%, #e9e9ea 100%);
    border-top: 4px solid var(--rule);
    display: flex; flex-direction: column; justify-content: center; align-items: center;
  }
  .intro-band p { font-weight: 500; font-size: 80px; line-height: 1.08; color: var(--ink-dark); white-space: nowrap; }

  /* Photo grid */
  .photo-grid { left: 0; top: 1084px; width: 1200px; height: 1090px; }

  /* Use tags */
  .tags { left: 0; top: 2208px; width: 1200px; height: 220px; }
  .tag-label {
    font-family: "Saira Condensed", sans-serif; font-weight: 600; font-size: 66px; fill: #fff;
  }

  .rule { left: 0; top: 2464px; width: 1200px; height: 4px; background: var(--rule); }

  /* Paving message */
  .paving { left: 0; top: 2510px; width: 1200px; height: 250px; }
  .paving-text {
    left: 330px; top: 2545px; width: 540px; text-align: center;
    font-weight: 500; font-size: 78px; line-height: 1.12; color: var(--ink-dark);
  }

  /* Certification */
  .cert-caption {
    left: 0; top: 2800px; width: 1200px; text-align: center;
    font-weight: 700; font-size: 22px; letter-spacing: 1px; color: var(--ink-dark);
    text-transform: uppercase;
  }
  .cert-name {
    left: 0; top: 2832px; width: 1200px; text-align: center;
    font-family: "Saira", sans-serif; font-weight: 800; font-size: 92px; line-height: 1;
    color: var(--deep-blue);
  }

  .footer-wave { left: 0; top: 2975px; width: 1200px; height: 122px; }
</style>
</head>
<body>

  <svg class="abs brand-banner" viewBox="0 0 684 310" aria-hidden="true">
    <polygon points="0,0 684,0 684,250 342,310 0,250" fill="#ffffff"/>
  </svg>
  <div class="abs brand-name">SOLIDE TRAJET</div>
  <div class="abs brand-tagline">100% béton décoratif</div>

  <h1>
    <span class="abs title-beton">Beton</span>
    <span class="abs title-imprime">IMPRIMÉ</span>
  </h1>
  <div class="abs catchphrase">Des sols uniques</div>

  <section class="abs intro-band">
    <p>Grand nombre de couleurs et textures...</p>
    <p>des milliers de possibilités</p>
  </section>

  <svg class="abs photo-grid" viewBox="0 0 1200 1090">
    <defs>
      <linearGradient id="pool-compass" x1="0" y1="0" x2="0" y2="1">
        <stop offset="0" stop-color="#3d9bc0"/><stop offset="0.25" stop-color="#8aa8a8"/>
        <stop offset="0.4" stop-color="#c2b299"/><stop offset="1" stop-color="#a89478"/>
      </linearGradient>
      <linearGradient id="wood-deck" x1="0" y1="0" x2="1" y2="1">
        <stop offset="0" stop-color="#3f8eb0"/><stop offset="0.3" stop-color="#6f7b86"/>
        <stop offset="1" stop-color="#4d545c"/>
      </linearGradient>
      <linearGradient id="roundabout" x1="0" y1="0" x2="0" y2="1">
        <stop offset="0" stop-color="#9fa7a4"/><stop offset="0.3" stop-color="#6c7a5a"/>
        <stop offset="0.5" stop-color="#9c5040"/><stop offset="1" stop-color="#7e3f33"/>
      </linearGradient>
      <linearGradient id="stamping" x1="0" y1="0" x2="1" y2="1">
        <stop offset="0" stop-color="#c2741e"/><stop offset="0.4" stop-color="#e6c21a"/>
        <stop offset="1" stop-color="#d8641c"/>
      </linearGradient>
    </defs>
    <polygon role="img" aria-label="Terrasse de piscine en béton imprimé avec rose des vents" points="0,0 520,0 580,521 0,521" fill="url(#pool-compass)"/>
    <polygon role="img" aria-label="Plage de piscine en béton imprimé effet planches de bois" points="530,0 1200,0 1200,521 590,521" fill="url(#wood-deck)"/>
    <polygon role="img" aria-label="Rond-point en béton imprimé rouge avec étoile et arbre central" points="0,541 615,541 676,1088 0,1088" fill="url(#roundabout)"/>
    <polygon role="img" aria-label="Ouvrier appliquant une matrice d'impression jaune sur béton orange" points="625,541 1200,541 1200,1088 686,1088" fill="url(#stamping)"/>
  </svg>

  <svg class="abs tags" viewBox="0 0 1200 220" aria-label="Domaines d'application">
    <polygon points="0,3 650,3 676,50 650,96 0,96" fill="var(--tag-dark)"/>
    <text class="tag-label" x="20" y="72">Aménagements urbains</text>
    <polygon points="710,3 1200,3 1200,96 710,96 736,50" fill="var(--tag-green)"/>
    <text class="tag-label" x="960" y="72" text-anchor="middle">Parcs à thèmes</text>

    <polygon points="0,122 310,122 336,168 310,216 0,216" fill="var(--tag-green)"/>
    <text class="tag-label" x="155" y="191" text-anchor="middle">Terrasses</text>
    <polygon points="361,122 689,122 670,216 361,216 382,168" fill="var(--tag-blue)"/>
    <text class="tag-label" x="528" y="191" text-anchor="middle">Piscines</text>
    <polygon points="715,122 942,122 922,216 715,216 696,168" fill="var(--tag-orange)"/>
    <text class="tag-label" x="818" y="191" text-anchor="middle">Plages</text>
    <polygon points="980,122 1200,122 1200,216 980,216 960,168" fill="var(--tag-grey)"/>
    <text class="tag-label" x="1090" y="191" text-anchor="middle">Allées</text>
  </svg>

  <div class="abs rule"></div>

  <svg class="abs paving" viewBox="0 0 1200 250">
    <defs>
      <linearGradient id="old-pavers" x1="0" y1="0" x2="1" y2="1">
        <stop offset="0" stop-color="#c9bf8f"/><stop offset="1" stop-color="#9c9474"/>
      </linearGradient>
      <linearGradient id="stamped-slab" x1="0" y1="0" x2="1" y2="1">
        <stop offset="0" stop-color="#8f8a84"/><stop offset="1" stop-color="#6b6661"/>
      </linearGradient>
    </defs>
    <rect role="img" aria-label="Pavés soulevés et déchaussés" x="57" y="13" width="222" height="217" fill="url(#old-pavers)" stroke="#fff" stroke-width="6"/>
    <line x1="70" y1="28" x2="266" y2="216" stroke="var(--cross-red)" stroke-width="14" stroke-linecap="round"/>
    <path d="M300 122 h22 M312 112 l12 10 l-12 10" fill="none" stroke="var(--ink-dark)" stroke-width="5"/>
    <path d="M874 122 h22 M886 112 l12 10 l-12 10" fill="none" stroke="var(--ink-dark)" stroke-width="5"/>
    <rect role="img" aria-label="Dalle monolithique en béton imprimé effet pavés" x="916" y="13" width="224" height="217" fill="url(#stamped-slab)" stroke="#fff" stroke-width="6"/>
  </svg>
  <div class="abs paving-text">Fini les pavés<br>qui déchaussent !</div>

  <div class="abs cert-caption">Classement performanciel</div>
  <div class="abs cert-name">RVQL</div>

  <svg class="abs footer-wave" viewBox="0 0 1200 122" preserveAspectRatio="none" aria-hidden="true">
    <path d="M0 122 L0 80 Q600 -10 1200 80 L1200 122 Z" fill="var(--deep-blue)"/>
  </svg>

</body>
</html>
```